Business Card for my New Brokerage

Looking to get a business card design for my new Real Estate Brokerage.
I want it with Picture, Phone Number, Email, Website, Office Address
Name and Designation. Please add logo too.

Target Market(s)

Real Estate Investors or Home Buyers

Industry/Entity Type

Real Estate

Contact Information for Business Card

Name, Email, Phone Number, website, email, office address

Colors
EB3D1F
EC4F4E
F09395
F8D3D4
FCEDEE

Requirements
Must have
• Minimalistic, Clean, Modern, Photo
Nice to have
• White and Red Colors

```html
<!DOCTYPE html>
<html lang="en">
<head>
<meta charset="utf-8">
<title>Ember Realty Inc — Business Card</title>
<link href="https://fonts.googleapis.com/css2?family=Outfit:wght@400;500;600&display=swap" rel="stylesheet">
<style>
  :root {
    --stage: #100e48;
    --card: #ffffff;
    --brand-red: #df1f26;
    --gold-dark: #b8862f;
    --gold-light: #f3e39a;
    --ink: #2b2b2b;
    --photo-light: #fbfaf8;
    --photo-mid: #eeece9;
    --photo-deep: #dfe2ea;
  }
  * { box-sizing: border-box; margin: 0; padding: 0; }
  html, body {
    width: 1200px;
    height: 1000px;
    overflow: hidden;
    background: var(--stage);
    font-family: "Outfit", sans-serif;
  }
  .card {
    position: absolute;
    left: 348px;
    width: 504px;
    height: 288px;
    background: var(--card);
    box-shadow: 0 4px 14px rgba(0, 0, 0, 0.35);
    overflow: hidden;
  }
  .card--front { top: 185px; }
  .card--back { top: 526px; }

  /* Front */
  .property-photo {
    position: absolute;
    inset: 0;
    clip-path: polygon(268px 0, 504px 0, 504px 288px, 0 288px);
    background:
      linear-gradient(180deg, rgba(255,255,255,0) 55%, rgba(210,216,230,0.55) 100%),
      linear-gradient(90deg, var(--photo-light) 0%, var(--photo-mid) 60%, var(--photo-deep) 100%);
  }
  .diagonal-band {
    position: absolute;
    inset: 0;
    width: 504px;
    height: 288px;
  }

  .wordmark {
    position: absolute;
    color: var(--brand-red);
    line-height: 1;
    text-align: center;
  }
  .wordmark__name { display: block; font-weight: 600; letter-spacing: 1px; }
  .wordmark__sub { display: block; font-weight: 400; }

  .card--front .wordmark { left: 226px; top: 112px; width: 250px; }
  .card--front .wordmark__name { font-size: 64px; }
  .card--front .wordmark__sub { font-size: 21px; letter-spacing: 6px; margin-top: 8px; }

  /* Back */
  .card--back .wordmark { left: 34px; top: 92px; width: 190px; }
  .card--back .wordmark__name { font-size: 48px; }
  .card--back .wordmark__sub { font-size: 15px; letter-spacing: 4px; margin-top: 6px; }

  .person {
    position: absolute;
    left: 283px;
    top: 44px;
  }
  .person__name {
    color: var(--brand-red);
    font-weight: 600;
    font-size: 16.5px;
    letter-spacing: -0.1px;
  }
  .person__title {
    color: var(--ink);
    font-size: 12.5px;
    margin-top: 5px;
  }

  .contact-list {
    position: absolute;
    left: 276px;
    top: 164px;
    list-style: none;
  }
  .contact-list li,
  .address {
    display: flex;
    align-items: center;
    height: 24px;
    color: var(--ink);
    font-size: 12.5px;
  }
  .icon {
    width: 20px;
    height: 20px;
    flex: none;
    margin-right: 11px;
  }
  .address {
    position: absolute;
    left: 36px;
    top: 210px;
    align-items: flex-start;
    height: auto;
    line-height: 1.25;
  }
</style>
</head>
<body>

<section class="card card--front" aria-label="Card front">
  <div class="property-photo" role="img" aria-label="Softly faded photograph of a white Mediterranean-style house with a pool"></div>
  <svg class="diagonal-band" viewBox="0 0 504 288" aria-hidden="true">
    <defs>
      <linearGradient id="gold-edge" x1="0" y1="1" x2="1" y2="0">
        <stop offset="0" stop-color="var(--gold-dark)"/>
        <stop offset="0.45" stop-color="var(--gold-light)"/>
        <stop offset="1" stop-color="var(--gold-dark)"/>
      </linearGradient>
    </defs>
    <polygon points="201,0 207,0 0,222 0,215" fill="url(#gold-edge)"/>
    <polygon points="207,0 268,0 0,288 0,222" fill="var(--brand-red)"/>
  </svg>
  <div class="wordmark">
    <span class="wordmark__name">EMBER</span>
    <span class="wordmark__sub">REALTY INC</span>
  </div>
</section>

<section class="card card--back" aria-label="Card back">
  <div class="wordmark">
    <span class="wordmark__name">EMBER</span>
    <span class="wordmark__sub">REALTY INC</span>
  </div>

  <div class="person">
    <p class="person__name">FIRST AND SECOND NAME</p>
    <p class="person__title">Full title of person</p>
  </div>

  <div class="address">
    <svg class="icon" viewBox="0 0 20 20" aria-hidden="true">
      <circle cx="10" cy="10" r="10" fill="var(--brand-red)"/>
      <path d="M10 4.5a3.3 3.3 0 0 0-3.3 3.3c0 2.5 3.3 6.4 3.3 6.4s3.3-3.9 3.3-6.4A3.3 3.3 0 0 0 10 4.5z" fill="#fff"/>
      <circle cx="10" cy="7.8" r="1.2" fill="var(--brand-red)"/>
    </svg>
    <p>Place, City, Distric, State<br>fulladdress line</p>
  </div>

  <ul class="contact-list">
    <li>
      <svg class="icon" viewBox="0 0 20 20" aria-hidden="true">
        <circle cx="10" cy="10" r="10" fill="var(--brand-red)"/>
        <path d="M7 5.5l1.6 2.2-.9 1.1c.6 1.3 1.4 2.1 2.6 2.7l1.1-.9 2.2 1.5-.8 1.8c-3.6-.2-6.4-3.1-6.6-6.6z" fill="#fff"/>
      </svg>
      +0 123 456 789
    </li>
    <li>
      <svg class="icon" viewBox="0 0 20 20" aria-hidden="true">
        <circle cx="10" cy="10" r="10" fill="var(--brand-red)"/>
        <rect x="7.3" y="5" width="5.4" height="10" rx="1" fill="#fff"/>
        <rect x="8.3" y="6.3" width="3.4" height="6" fill="var(--brand-red)"/>
      </svg>
      123456789
    </li>
    <li>
      <svg class="icon" viewBox="0 0 20 20" aria-hidden="true">
        <circle cx="10" cy="10" r="10" fill="var(--brand-red)"/>
        <rect x="5.8" y="7" width="8.4" height="6" rx="0.8" fill="#fff"/>
        <path d="M6 7.4l4 3 4-3" fill="none" stroke="var(--brand-red)" stroke-width="0.9"/>
      </svg>
      name@email.com
    </li>
    <li>
      <svg class="icon" viewBox="0 0 20 20" aria-hidden="true">
        <circle cx="10" cy="10" r="10" fill="var(--brand-red)"/>
        <g fill="none" stroke="#fff" stroke-width="0.9">
          <circle cx="10" cy="10" r="4.4"/>
          <ellipse cx="10" cy="10" rx="1.9" ry="4.4"/>
          <path d="M5.6 10h8.8M6.3 7.8h7.4M6.3 12.2h7.4"/>
        </g>
      </svg>
      www.domainname.com
    </li>
  </ul>
</section>

</body>
</html>
```